High End Personalized Functional Medicine in Women's Health

We are adding new and exciting personalized medicine services to our Women's Health Care practice focusing on health optimization and anti-aging as well as hormone replacement therapy and need a high end brochure to educate patients about these services. We would like to see a zen-like design that has feminine appeal. Our office colors are vibrant but soothing. We have utilized the concepts of feng shui to optimize our positive energy. The exterior of the building is peach and cream and these colors would blend with that energy The final design should communicate a sense that you can take control of your health and aging.
Updates

Target Market(s)

Females age 35-65 with annual income >$75000/year

Industry/Entity Type

Health And Wellness

Logo Text

Bright Path is the company name. Our sister company is Mesa Rio Ob/Gyn

Font styles to use
Serif

Colors

Designer to choose colors to be used in the design.

Requirements
Must have
• My project must have clean lines. I like a strong feminine appearance, not a fluffy curvy feminine look. Professional appearance, Brochure would be on thicker card stock. A strong front page that makes you want to open the brochure
Nice to have
• Eye catching photos that complement our message . I am not tied to the peach and cream color recommendation, but find those colors feminine but not so cliche as pinks and purples.
Should not have
• frilly design

```html
<!DOCTYPE html>
<html lang="en">
<head>
<meta charset="utf-8">
<title>Bright Path – Personalized Women's Health</title>
<link rel="stylesheet" href="https://fonts.googleapis.com/css2?family=Playfair+Display:wght@700&family=Lora:wght@400;500&display=swap">
<style>
  :root {
    --stage: #efe9e2;
    --cream: #fbf5ec;
    --peach: #f2b89f;
    --peach-soft: #f7d6c6;
    --terracotta: #c26e52;
    --clay: #5b4a42;
    --ink: #3d3530;
    --photo-light: #f1ede8;
    --photo-mid: #ddd6cf;
    --photo-blue-a: #dbe9ef;
    --photo-blue-b: #9fc4d6;
  }
  * { box-sizing: border-box; margin: 0; padding: 0; }
  html, body { width: 1200px; height: 861px; overflow: hidden; background: var(--stage); }
  .brochure {
    position: absolute; left: 310px; top: 20px; width: 580px; height: 820px;
    background: var(--cream); overflow: hidden;
    box-shadow: 0 6px 18px rgba(61,53,48,.16);
  }
  .brochure-art { position: absolute; inset: 0; width: 580px; height: 820px; }
  .section-title {
    position: absolute; font-family: "Playfair Display", serif; font-weight: 700;
    font-size: 20px; line-height: 1; letter-spacing: 1px; color: var(--terracotta);
  }
  .section-body {
    position: absolute; width: 250px; font-family: "Lora", serif;
    font-size: 9.5px; line-height: 13px; color: var(--ink); text-align: justify;
  }
  .contact { position: absolute; right: 22px; top: 716px; text-align: right; color: var(--cream); font-family: "Lora", serif; }
  .contact-title { font-family: "Playfair Display", serif; font-weight: 700; font-size: 17px; letter-spacing: 1px; margin-bottom: 8px; }
  .contact-line { display: flex; align-items: center; justify-content: flex-end; gap: 12px; font-size: 13px; height: 22px; }
  .contact-icon { width: 13px; height: 13px; flex: none; }
</style>
</head>
<body>
<main class="brochure">
  <svg class="brochure-art" viewBox="0 0 580 820">
    <defs>
      <linearGradient id="officeTone" x1="0" y1="0" x2="1" y2="1">
        <stop offset="0" stop-color="var(--photo-light)"/>
        <stop offset="1" stop-color="var(--photo-mid)"/>
      </linearGradient>
      <linearGradient id="careTone" x1="0" y1="0" x2="1" y2="1">
        <stop offset="0" stop-color="var(--photo-blue-a)"/>
        <stop offset="1" stop-color="var(--photo-blue-b)"/>
      </linearGradient>
    </defs>

    <polygon class="hero-photo" role="img" aria-label="Photo of a doctor in a white coat writing at her desk in a bright clinic office"
             fill="url(#officeTone)" points="0,0 580,0 580,250 0,330"/>
    <line class="accent-line" x1="0" y1="346" x2="580" y2="266" stroke="var(--peach)" stroke-width="5"/>
    <line class="accent-line" x1="0" y1="362" x2="300" y2="320" stroke="var(--clay)" stroke-width="2"/>

    <circle cx="420" cy="404" r="121" fill="var(--cream)"/>
    <circle cx="420" cy="404" r="114" fill="none" stroke="var(--terracotta)" stroke-width="3"/>
    <circle class="care-photo" role="img" aria-label="Photo of a nurse in blue scrubs comforting a smiling elderly patient"
            cx="420" cy="404" r="108" fill="url(#careTone)"/>

    <line class="accent-line" x1="0" y1="786" x2="580" y2="666" stroke="var(--peach)" stroke-width="4"/>
    <polygon class="footer-band" fill="var(--terracotta)" points="0,820 0,800 580,680 580,820"/>
  </svg>

  <h2 class="section-title" style="left:22px; top:445px;">VITAL BALANCE</h2>
  <p class="section-body" style="left:22px; top:473px;">Our personalized functional medicine program looks at the whole woman. We study your history, lab results, sleep, nutrition and stress to understand what your body needs, then build a clear plan that helps you feel strong, focused and well in every season of life. Care is calm, unhurried and always tailored to you.</p>

  <h2 class="section-title" style="left:22px; top:600px;">AGE WELL</h2>
  <p class="section-body" style="left:22px; top:628px;">Healthy aging begins with knowing where you stand today. We pair advanced testing with practical guidance on movement, diet and rest, so you can protect your energy, skin, bones and heart and take control of how you age.</p>

  <h2 class="section-title" style="left:309px; top:530px;">HORMONE CARE</h2>
  <p class="section-body" style="left:309px; top:558px;">Shifting hormones can change your mood, sleep, weight and energy. Our hormone replacement therapy starts with a careful review of your symptoms and lab work. Together we choose the right approach, monitor your progress closely and adjust your plan as your body changes, always with safety first. Many women find renewed balance, better rest and a steadier sense of self.</p>

  <section class="contact">
    <h3 class="contact-title">CONTACT US</h3>
    <div class="contact-line">+1 505 555 0142
      <svg class="contact-icon" viewBox="0 0 16 16"><circle cx="8" cy="8" r="7" fill="none" stroke="#fbf5ec" stroke-width="1.4"/><path d="M5.6 4.5c.5-.3 1 .1 1.2.6l.4.9c.1.4 0 .7-.3.9l-.4.3c.4.9 1.1 1.6 2 2l.3-.4c.2-.3.6-.4.9-.3l.9.4c.5.2.9.7.6 1.2-.4.8-1.2 1.1-2 .8C7.3 10.2 5.8 8.7 5 6.7c-.3-.9 0-1.8.6-2.2z" fill="#fbf5ec"/></svg>
    </div>
    <div class="contact-line">hello@brightpath.example
      <svg class="contact-icon" viewBox="0 0 16 16"><circle cx="8" cy="8" r="8" fill="#fbf5ec"/><rect x="4" y="5.2" width="8" height="5.6" rx=".6" fill="var(--terracotta)"/><path d="M4.3 5.6 8 8.4l3.7-2.8" fill="none" stroke="#fbf5ec" stroke-width=".8"/></svg>
    </div>
    <div class="contact-line">www.brightpath.example
      <svg class="contact-icon" viewBox="0 0 16 16"><circle cx="8" cy="8" r="8" fill="#fbf5ec"/><g fill="none" stroke="var(--terracotta)" stroke-width=".9"><circle cx="8" cy="8" r="4.6"/><ellipse cx="8" cy="8" rx="2" ry="4.6"/><path d="M3.4 8h9.2"/></g></svg>
    </div>
  </section>
</main>
</body>
</html>
```